New Health Business Needs Flyer for Africa

We are a new network marketing company about to launch in Africa. I need a flyer made purely for the business and earning opportunity that people can get with our company. This is a home based business that anyone can get involved with. Very low start up costs with high quality effective and innovative products. You can visit our blog to get more information on the benefits I would like to see on the flyer. http://qelvorinotes.com. This flyer is to attract people who want to earn more money and build a long term business with financial security.
Updates

This needs to be about making more money. Luxury lifestyle, flash cars, big houses etc. I don't want anything about the product on this flyer

Reason: to give you all a bit more time on this I have extended the time period

Reason: to give you more time

Target Market(s)

anyone who wants to earn more money. Over 18 years old.

Industry/Entity Type

Marketing

Requirements
Must have
• This is a simple handout flyer A5 size. Can have front and back. Because we are opening in Africa, any faces or people should be black. It should have the logo which is uploaded to files also.

```html
<!DOCTYPE html>
<html lang="en">
<head>
<meta charset="utf-8">
<title>Kelvani International – Earn More Money Flyer</title>
<link rel="stylesheet" href="https://fonts.googleapis.com/css2?family=Didact+Gothic&family=Mulish:wght@800&display=swap">
<style>
  :root {
    --page-bg: #ffffff;
    --sheet-top: #f7f7f7;
    --sheet-bottom: #d9d9d9;
    --sheet-edge: #b9b9b9;
    --brand-blue: #1f3fd8;
    --brand-green: #33dd00;
    --url-grey: #4a4a4a;
    --photo-light: #aab8c4;
    --photo-dark: #4d4f55;
  }
  * { box-sizing: border-box; margin: 0; padding: 0; }
  html, body {
    width: 910px; height: 1200px; overflow: hidden;
    background: var(--page-bg);
  }
  .canvas { position: relative; width: 910px; height: 1200px; }
  .flyer {
    position: absolute; left: 85px; top: 77px;
    width: 650px; height: 920px;
    transform: scale(1.1375); transform-origin: 0 0;
    background: radial-gradient(ellipse at 40% 55%, var(--sheet-top) 0%, #ececec 55%, var(--sheet-bottom) 100%);
    border: 1px solid var(--sheet-edge);
    overflow: hidden;
    font-family: "Didact Gothic", "Century Gothic", sans-serif;
  }
  .flyer__backdrop, .flyer__hero { position: absolute; left: 0; top: 0; width: 650px; height: 920px; }
  .brand {
    position: absolute; left: 22px; top: 410px;
    color: var(--brand-blue); font-weight: 400;
    line-height: 1;
  }
  .brand__name { display: block; font-size: 70px; letter-spacing: -1px; }
  .brand__tag { display: block; font-size: 19px; margin: -4px 0 0 165px; }
  .headline {
    position: absolute; left: 28px; top: 528px; width: 600px;
    font-family: "Mulish", "Century Gothic", sans-serif; font-weight: 800;
    font-size: 37.5px; color: var(--brand-green); letter-spacing: 0.2px;
    white-space: nowrap;
  }
  .intro {
    position: absolute; left: 32px; top: 590px; width: 582px;
    color: var(--brand-blue); font-size: 16.6px; line-height: 19px;
    text-align: justify;
  }
  .intro__lead { font-size: 37px; line-height: 36px; }
  .benefits {
    position: absolute; left: 42px; top: 724px; list-style: none;
    color: var(--brand-green); font-size: 25px; line-height: 40px;
  }
  .benefits li { display: flex; align-items: center; }
  .benefits li::before {
    content: ""; width: 9px; height: 9px; border-radius: 50%;
    background: var(--brand-green); margin: 6px 6px 0 0; flex: none;
  }
  .web-address {
    position: absolute; right: 22px; top: 866px;
    color: var(--url-grey); font-size: 28px; letter-spacing: 0.3px;
  }
</style>
</head>
<body>
<div class="canvas">
  <article class="flyer">
    <svg class="flyer__backdrop" viewBox="0 0 650 920" aria-hidden="true">
      <path d="M22 250 C90 330 40 380 110 470 C220 600 260 760 170 900 C330 780 330 560 190 430 C120 370 60 330 22 250 Z" fill="#ffffff" opacity="0.6"/>
    </svg>

    <svg class="flyer__hero" viewBox="0 0 650 920" role="img" aria-label="Photo of a smiling young woman holding a piggy bank stuffed with banknotes">
      <defs>
        <linearGradient id="hero-tones" x1="0" y1="0" x2="1" y2="0.4">
          <stop offset="0" stop-color="var(--photo-light)"/>
          <stop offset="0.55" stop-color="#b8c3cc"/>
          <stop offset="1" stop-color="var(--photo-dark)"/>
        </linearGradient>
      </defs>
      <path d="M22 0 H650 V400 Q560 436 420 432 Q230 424 110 345 Q40 295 22 220 Z" fill="url(#hero-tones)"/>
      <path d="M650 400 Q560 436 420 432 Q230 424 110 345 Q70 315 52 285" fill="none" stroke="var(--brand-green)" stroke-width="3"/>
    </svg>

    <div class="brand">
      <span class="brand__name">kelvani</span>
      <span class="brand__tag">international</span>
    </div>

    <h1 class="headline">Want To Earn More Money?</h1>

    <p class="intro"><span class="intro__lead">Lorem ipsum dolor</span> sit amet, consectetuer adipiscing elit. Nam cursus. Morbi ut mi. Nullam enim leo, egestas id, condimentum at, laoreet mattis, massa. Sed eleifend non­ummy diam. Praesent mauris ante, elementum et, bibendum at,</p>

    <ul class="benefits">
      <li>Morbi magna magna, tincidunt</li>
      <li>Non, imperdiet vitae, tellus. Sed odi</li>
      <li>Uctor ac, sollicitudin in, consequat</li>
    </ul>

    <p class="web-address">www.qelvorinotes.com</p>
  </article>
</div>
</body>
</html>
```